Goodlooking website for a company who is working in the IT consultancy

We want a new website designed in WordPress. You can take www.dravek.nl as an example. It should be a website with some short blocks of information about the company, nice pictures of our partners and our employees. A job page with a clear filter.

Target Market(s)

B2B

Industry/Entity Type

It Company

Coding

Coded - Design and coding required

Number of Pages Required

5+ page

Font styles to use
Sans Serif

Colors
0455a3
34a7d8

Requirements
Must have
• Check briefing

```html
<!DOCTYPE html>
<html lang="en">
<head>
<meta charset="utf-8">
<title>Dravek – IT Consultancy</title>
<link href="https://fonts.googleapis.com/css2?family=Mulish:wght@400;600;700&display=swap" rel="stylesheet">
<style>
:root{
  --teal:#4cc0a6;
  --sky:#3db7d9;
  --slate:#3e6670;
  --navy:#163640;
  --ink:#2a3942;
  --text:#222;
  --muted:#9a9a9a;
  --light:#f3f3f3;
  --row:#f4f4f4;
  --line:#dcdcdc;
  --footer:#4b5057;
  --about:#2ea3cc;
}
*{box-sizing:border-box;margin:0;padding:0}
html,body{width:1200px;height:4286px;overflow:hidden}
body{font-family:"Mulish",Arial,sans-serif;color:var(--text);background:#fff;position:relative}
section,header,footer{position:relative;width:1200px}
.brand{display:flex;align-items:center;gap:10px;font-weight:700;font-size:24px;letter-spacing:2px}
.brand-dot{width:30px;height:30px;border-radius:50%;background:var(--slate)}

/* header */
.site-header{height:80px;display:flex;align-items:center;justify-content:space-between;padding:0 100px}
.site-header .brand{color:var(--slate)}
.main-nav{display:flex;gap:32px;font-size:15px;font-weight:600;color:#222}
.main-nav .active{color:var(--teal)}

/* hero */
.hero{height:560px;overflow:hidden}
.hero-photo{position:absolute;inset:0;background:linear-gradient(135deg,#5b5750 0%,#3c3b3a 45%,#6a6156 75%,#4b4640 100%)}
.hero-content{position:absolute;left:0;right:0;top:240px;text-align:center;color:#fff}
.hero-title{font-size:38px;font-weight:400}
.btn{display:inline-block;text-transform:uppercase;font-weight:700;font-size:13px;color:#fff;border-radius:4px;text-align:center}
.hero .btn{background:var(--sky);width:190px;height:46px;line-height:46px;margin-top:28px}

/* headings */
.section-title{text-align:center;font-size:36px;font-weight:400;color:#111}

/* offer */
.offer{height:520px}
.offer .section-title{padding-top:76px}
.offer-list{display:flex;justify-content:center;gap:200px;margin-top:54px}
.offer-item{width:200px;text-align:center}
.offer-icon{width:136px;height:136px;border-radius:50%;margin:0 auto;display:flex;align-items:center;justify-content:center}
.offer-item h3{font-size:17px;font-weight:600;color:var(--navy);margin-top:33px}
.offer-item p{font-size:12px;line-height:17px;color:var(--muted);margin-top:22px}

/* jobs */
.jobs{height:760px}
.jobs .section-title{padding-top:65px}
.job-table{position:absolute;left:110px;top:145px;width:980px;border:1px solid var(--line)}
.job-row{height:73px;display:flex;align-items:center;justify-content:space-between;padding:0 30px 0 30px;font-size:14px;font-weight:600;color:var(--navy);border-bottom:1px solid var(--line);background:#fff}
.job-row:nth-child(odd){background:var(--row)}
.job-row:first-child{background:var(--navy);color:#fff}
.job-row:last-child{border-bottom:none}
.job-row .btn{background:var(--teal);width:146px;height:36px;line-height:36px;font-size:12px;margin-right:-10px}

/* about */
.about{height:546px;overflow:hidden}
.about-photo{position:absolute;inset:0;background:linear-gradient(120deg,#2b9cc6 0%,#35a8d2 45%,#2790bd 100%)}
.about-content{position:absolute;left:150px;right:150px;top:110px;text-align:center;color:#fff}
.about-content .section-title{color:#fff}
.about-content p{font-size:13px;line-height:26px;margin-top:22px}
.about-content p:first-of-type{margin-top:30px}
.about .btn{background:var(--navy);width:145px;height:38px;line-height:38px;margin-top:30px;font-size:12px}

/* what we do */
.services{height:934px}
.services .section-title{padding-top:88px}
.services svg{position:absolute;left:279px;top:185px}

/* contact */
.contact{height:608px;background:var(--light)}
.contact .section-title{padding-top:54px}
.contact-form{position:absolute;left:200px;top:170px;width:798px;display:grid;grid-template-columns:387px 387px;column-gap:24px;row-gap:20px}
.field{height:60px;background:#fff;border:1px solid #d6d6d6;font-size:12px;color:#777;padding:20px 22px}
.field-message{grid-column:1/3;height:135px;margin-top:7px}
.contact .btn{position:absolute;left:478px;top:510px;width:244px;height:48px;line-height:48px;background:var(--sky);font-size:13px}

/* partners */
.partners{height:152px;text-align:center}
.partners h4{font-size:17px;font-weight:700;padding-top:38px}
.partner-list{display:flex;justify-content:center;align-items:center;gap:34px;margin-top:22px}
.partner-badge{background:#d9dde1}

/* footer */
.site-footer{height:126px;background:var(--footer);color:#fff;display:flex;align-items:center;padding:0 40px 0 100px;font-size:12px}
.site-footer .brand{font-size:22px}
.site-footer .brand-dot{background:#fff}
.footer-nav{display:flex;gap:22px;margin-left:28px}
.social{display:flex;gap:12px;margin-left:112px}
.social span{width:14px;height:14px;border-radius:50%;background:#fff}
.copyright{margin-left:26px}
.lang{margin-left:auto}
</style>
</head>
<body>

<header class="site-header">
  <div class="brand"><span class="brand-dot"></span>DRAVEK</div>
  <nav class="main-nav">
    <span class="active">Home</span><span>Oplossingen</span><span>Ons Team</span><span>Partners</span><span>Vacatures</span><span>Contact</span>
  </nav>
</header>

<section class="hero">
  <div class="hero-photo" role="img" aria-label="Photo of a smiling team of consultants in an office, darkened"></div>
  <div class="hero-content">
    <h1 class="hero-title">We build mission critical environments</h1>
    <span class="btn">Learn More</span>
  </div>
</section>

<section class="offer">
  <h2 class="section-title">What We Offer</h2>
  <div class="offer-list">
    <div class="offer-item">
      <div class="offer-icon" style="background:var(--sky)">
        <svg width="64" height="64" viewBox="0 0 64 64" fill="none" stroke="#0f2a33" stroke-width="3"><rect x="22" y="10" width="34" height="26"/><polyline points="28,30 36,22 42,27 50,16"/><circle cx="12" cy="16" r="5"/><path d="M6 54V30h12l8-6M18 30v24M6 54h50"/></svg>
      </div>
      <h3>Training</h3>
      <p>Practical sessions that sharpen the skills your teams use every day, led by consultants who work on live environments and share what truly holds up.</p>
    </div>
    <div class="offer-item">
      <div class="offer-icon" style="background:var(--teal)">
        <svg width="64" height="64" viewBox="0 0 64 64" fill="none" stroke="#0f2a33" stroke-width="3"><rect x="18" y="10" width="28" height="30" rx="12"/><path d="M8 58c0-12 10-16 24-16s24 4 24 16"/><path d="M28 42l4 10 4-10"/></svg>
      </div>
      <h3>Personal Coaching</h3>
      <p>One to one guidance for engineers and leads who want to grow, with clear goals, honest feedback and steady support through every phase of the path.</p>
    </div>
    <div class="offer-item">
      <div class="offer-icon" style="background:var(--slate)">
        <svg width="64" height="64" viewBox="0 0 64 64" fill="#0f2a33"><path d="M18 8h28v14c0 9-6 16-14 16s-14-7-14-16z"/><path d="M18 12H8c0 10 5 14 11 14M46 12h10c0 10-5 14-11 14" fill="none" stroke="#0f2a33" stroke-width="3"/><rect x="29" y="38" width="6" height="10"/><rect x="20" y="48" width="24" height="8"/></svg>
      </div>
      <h3>Education Projects</h3>
      <p>Hands on projects built with schools and partners, so new talent learns by doing real work on systems that must stay online day and night.</p>
    </div>
  </div>
</section>

<section class="jobs">
  <h2 class="section-title">Jobs</h2>
  <div class="job-table">
    <div class="job-row"><span>IT Technology Consultant UI Designer Job</span><span class="btn">Apply Now</span></div>
    <div class="job-row"><span>IT Technology Consultant (developer) Job</span><span class="btn">Apply Now</span></div>
    <div class="job-row"><span>IT Technology Associate Consultant -backend Developer Job</span><span class="btn">Apply Now</span></div>
    <div class="job-row"><span>IT Architecture Senior Specialist-it Go-to-market Services Solution Centre</span><span class="btn">Apply Now</span></div>
    <div class="job-row"><span>US Junior IT Recruiter</span><span class="btn">Apply Now</span></div>
    <div class="job-row"><span>Sales/ Business Development Manager</span><span class="btn">Apply Now</span></div>
    <div class="job-row"><span>IT Project Manager - Scrum/agile</span><span class="btn">Apply Now</span></div>
  </div>
</section>

<section class="about">
  <div class="about-photo" role="img" aria-label="Photo of colleagues working on laptops, tinted blue"></div>
  <div class="about-content">
    <h2 class="section-title">About Us</h2>
    <p>We are a team of IT consultants who design, build and run environments that cannot fail. From first plan to daily operations we work side by side with your people, keep systems secure and available, and make sure every change is tested, documented and easy to hand over. Our clients rely on us when uptime matters most.</p>
    <p>Our approach is simple: listen first, choose proven technology and automate what can be automated. That leaves more time for the work that counts and gives your business a platform it can trust for years to come.</p>
    <span class="btn">Read More</span>
  </div>
</section>

<section class="services">
  <h2 class="section-title">What We Do</h2>
  <svg width="644" height="644" viewBox="0 0 644 644" font-family="Mulish, Arial, sans-serif" font-size="22" fill="#fff" text-anchor="middle">
    <defs><clipPath id="disc"><circle cx="322" cy="322" r="322"/></clipPath></defs>
    <g clip-path="url(#disc)">
      <rect x="0" y="0" width="315" height="315" fill="var(--sky)"/>
      <rect x="329" y="0" width="315" height="315" fill="var(--teal)"/>
      <rect x="0" y="329" width="315" height="315" fill="var(--navy)"/>
      <rect x="329" y="329" width="315" height="315" fill="var(--ink)"/>
    </g>
    <g fill="none" stroke="#fff" stroke-width="3">
      <rect x="156" y="112" width="94" height="62" rx="3"/><path d="M144 182h118"/><path d="M176 160v-16M192 160v-26M208 160v-20M224 160v-32"/>
      <path d="M456 170l14 14 46-56c6-8 8-18 6-24-6-2-16 0-24 6z"/><path d="M470 150l-18 2-10 14 18 2M490 170l-2 18-14 10-2-18M452 192l-10 10"/><circle cx="500" cy="124" r="6"/>
      <path d="M166 484v-22M184 484v-38M202 484v-30M220 484v-54M154 484h80"/><path d="M160 450l24-24 16 10 32-34M222 402h10v10"/>
      <path d="M452 420h30v-8a8 8 0 0116 0v8h30v30h-8a8 8 0 000 16h8v30h-30v-8a8 8 0 00-16 0v8h-30z"/>
    </g>
    <text x="205" y="237">Automation &amp;</text><text x="205" y="264">Deployment</text>
    <text x="440" y="237">Mission Critical</text><text x="440" y="264">Solutions</text>
    <text x="205" y="544">Mission Critical</text><text x="205" y="571">Solutions</text>
    <text x="440" y="544">Hyperconverged</text><text x="440" y="571">Infrastructures</text>
  </svg>
</section>

<section class="contact">
  <h2 class="section-title">Contact Us</h2>
  <div class="contact-form">
    <div class="field">Name</div>
    <div class="field">E-Mail</div>
    <div class="field">Phone</div>
    <div class="field">Location</div>
    <div class="field field-message">Message</div>
  </div>
  <span class="btn">Submit</span>
</section>

<section class="partners">
  <h4>Our Partnerships</h4>
  <div class="partner-list">
    <span class="partner-badge" style="width:78px;height:34px"></span>
    <span class="partner-badge" style="width:80px;height:40px"></span>
    <span class="partner-badge" style="width:84px;height:24px"></span>
    <span class="partner-badge" style="width:64px;height:56px;border-radius:50%"></span>
  </div>
</section>

<footer class="site-footer">
  <div class="brand"><span class="brand-dot"></span>DRAVEK</div>
  <nav class="footer-nav"><span>Home</span><span>Oplossingen</span><span>Ons Team</span><span>Partners</span><span>Vacatures</span><span>Contact</span></nav>
  <div class="social"><span></span><span></span></div>
  <span class="copyright">© 2018 Company Name | All Rights Reserved</span>
  <span class="lang">CS</span>
</footer>

</body>
</html>
```